Professional/modern business card design for construction company

We need a new business card design, double sided keeping it modern, sleek, professional and simple. We are an earthmoving business but do not want any pictures of machinery. I would like one side to have the logo and the other to have all the information, keeping with the colors in our logo. The business card will need to be able to be customised so we can use it for several different managers., we would also like to be able to use the design to apply it to other stationary ie. letterheads, notebooks etc. We do not really have a tag line but we could put on there that we specialise in - Agriculture, Civil Construction and Mining.

Contact Information for Business Card

Brolga Ridge Excavations Pty Ltd
ABN 58 402 937 615
82 Gumleaf Creek Road, Moree NSW 2400

Harold Benton
Managing Director
P 0418 639 204
E haroldbenton@brolgaridgeexc.com.au

Font styles to use
Serif
Sans Serif

Requirements
Nice to have
• I have attached some examples of ideas.
Should not have
• images of machinery

```html
<!DOCTYPE html>
<html lang="en">
<head>
<meta charset="utf-8">
<title>Brolga Ridge Excavations – Business Card</title>
<link rel="stylesheet" href="https://fonts.googleapis.com/css2?family=Roboto+Condensed:wght@400;700&display=swap">
<style>
  :root {
    --stage: #2b2b2b;
    --card-white: #ffffff;
    --charcoal: #434343;
    --orange: #f5841f;
    --text: #3a3a3a;
  }
  * { box-sizing: border-box; margin: 0; padding: 0; }
  html, body {
    width: 1200px; height: 900px; overflow: hidden;
    background: var(--stage);
    font-family: "Roboto Condensed", Arial, sans-serif;
  }
  .card {
    position: absolute; left: 261px; width: 656px; height: 357px; overflow: hidden;
  }
  .card--front { top: 69px; background: var(--card-white); }
  .card--back { top: 472px; background: var(--charcoal); }

  .swoosh { position: absolute; left: 0; top: 0; width: 656px; height: 357px; }

  .wordmark {
    position: absolute; display: flex; align-items: center; gap: 12px;
    font-weight: 700; text-transform: uppercase; line-height: 1.05; white-space: nowrap;
  }
  .wordmark__square { width: 20px; height: 20px; background: var(--orange); flex: none; }
  .card--front .wordmark { left: 37px; top: 155px; width: 260px; font-size: 23px; color: var(--charcoal); }
  .card--back .wordmark {
    left: 0; right: 0; top: 130px; justify-content: center;
    font-size: 40px; color: var(--card-white);
  }
  .card--back .wordmark__square { width: 30px; height: 30px; }

  .divider {
    position: absolute; left: 330px; top: 89px; width: 1.5px; height: 180px; background: var(--orange);
  }
  .contact { position: absolute; left: 360px; top: 82px; color: var(--text); font-size: 16px; }
  .contact__name {
    font-size: 35px; font-weight: 400; color: var(--orange); text-transform: uppercase;
    line-height: 1; letter-spacing: 0.2px;
  }
  .contact__role { margin-top: 3px; line-height: 1.2; }
  .contact__abn { margin-top: 9px; }
  .contact__address { margin-top: 8px; line-height: 1.18; }
  .contact__lines { margin-top: 8px; list-style: none; }
  .contact__lines li { display: flex; align-items: center; gap: 9px; height: 19px; }
  .contact__lines svg { width: 12px; height: 12px; flex: none; }
  .contact__web-domain { color: var(--orange); }
</style>
</head>
<body>
  <section class="card card--front" aria-label="Card front">
    <svg class="swoosh" viewBox="0 0 656 357" aria-hidden="true">
      <path d="M0 294 Q300 355 656 318 L656 357 L0 357 Z" fill="var(--charcoal)"/>
      <path d="M100 318 Q380 360 656 307 L656 320 Q380 352 100 318 Z" fill="var(--orange)"/>
    </svg>

    <div class="wordmark">
      <span class="wordmark__square"></span>
      <span>Brolga Ridge<br>Excavations Pty Ltd</span>
    </div>

    <div class="divider"></div>

    <div class="contact">
      <h1 class="contact__name">Harold Benton</h1>
      <p class="contact__role">Managing Director</p>
      <p class="contact__abn">ABN 58 402 937 615</p>
      <p class="contact__address">82 Gumleaf Creek Road,<br>Moree NSW 2400</p>
      <ul class="contact__lines">
        <li>
          <svg viewBox="0 0 12 12"><path d="M3 1 L5 3.5 L4 5 Q5 7.5 7 8 L8.5 7 L11 9 L9.5 11 Q3 10 1 2.5 Z" fill="none" stroke="var(--orange)" stroke-width="1"/></svg>
          0418 639 204
        </li>
        <li>
          <svg viewBox="0 0 12 12"><rect x="1" y="2.5" width="10" height="7" fill="none" stroke="var(--orange)" stroke-width="1"/><path d="M1 2.5 L6 6.5 L11 2.5" fill="none" stroke="var(--orange)" stroke-width="1"/></svg>
          haroldbenton@brolgaridgeexc.com.au
        </li>
        <li>
          <svg viewBox="0 0 12 12"><circle cx="6" cy="6" r="5" fill="none" stroke="var(--orange)" stroke-width="0.9"/><ellipse cx="6" cy="6" rx="2.2" ry="5" fill="none" stroke="var(--orange)" stroke-width="0.8"/><path d="M1 6 H11 M2 3.5 H10 M2 8.5 H10" stroke="var(--orange)" stroke-width="0.7"/></svg>
          <span>www.<span class="contact__web-domain">brolgaridgeexcavations</span>.com</span>
        </li>
      </ul>
    </div>
  </section>

  <section class="card card--back" aria-label="Card back">
    <div class="wordmark">
      <span class="wordmark__square"></span>
      <span>Brolga Ridge<br>Excavations Pty Ltd</span>
    </div>
  </section>
</body>
</html>
```